Banner for homepage

It is a new banner for the homepage, temporary site address is 61.187.40.72 ( is the biggest banner only ) . Would be 5 variations for image content as below (in Portuguese ) :

Image 1:
Leitor de codigo de barras
Todos os tipos de leitores de código de barras para as mais diversas aplicações.
( example of product images in : http://www.quentorlabs.com/en-US/Pages/Category.aspx?category=barcode-scanners&cat=KLT)

Image 2:
Impressora de etiquetas
Identifique o que for nessário com o melhor custo/beneficio e flexibilidade de materiais de impressão.
( example of product images in : vintor.com in label printers desktop and industrial)

Image 3:
Impressora de cupom
Imprima recibos e cupons fiscais com agilidade e qualidade, temos a impressora certa para o seu PDV.
( example of product images in : http://www.palutrek.com.br/equipamento-categoria-impressoras+fiscais.html)

Image 4:
Coletor de dados
Computadores móveis com leitor de código de barras, que levam a automação para frente de trabalho.
( example of product images in : http://www.quentorlabs.com/en-US/Pages/Category.aspx?cat=KLT&category=hand-held-mobile-computer)

Image 5:
Etiquetas e Ribbons:
Etiquetas adesivas e não adesivas em vários de tipos de materiais, papéis e plásticos. O ribbon certo para impressão perfeita em cada material.
( example of product images in : http://www.tagmirelo.com/cats/supplies/barcode-printer.htm?nav=hdr)

```html
<!DOCTYPE html>
<html lang="pt-BR">
<head>
<meta charset="utf-8">
<title>Travessa — Soluções em Automação e Código de barras</title>
<link rel="stylesheet" href="https://fonts.googleapis.com/css2?family=Oswald:wght@400;500&family=Bebas+Neue&family=Signika:wght@600&family=Arimo:wght@400;700&display=swap">
<style>
:root{
  --red:#c9353b;
  --red-dark:#a8262c;
  --page:#ebebeb;
  --nav:#3b3b3b;
  --nav-dark:#2a2a2a;
  --nav-text:#e6e6e6;
  --white:#ffffff;
  --ink:#3a3a3a;
  --accent:#e8502a;
  --yellow:#ffd21a;
  --yellow-dark:#f2a900;
  --sky:#a9cbe6;
  --tan:#c9a779;
  --box-dark:#3d3a38;
  --box-light:#8f817a;
}
*{box-sizing:border-box;margin:0;padding:0}
html,body{width:1200px;height:569px;overflow:hidden}
body{position:relative;background:var(--page);font-family:"Arimo",Arial,sans-serif}

.site-header{position:absolute;left:0;top:0;width:1200px;height:104px;
  background:linear-gradient(#d03c42,var(--red) 60%,#c0303a)}
.brand{position:absolute;left:103px;top:9px;width:289px;height:47px;display:flex;align-items:center;justify-content:center;
  background:var(--white);border-radius:24px}
.brand-name{font-family:"Arimo",Arial,sans-serif;font-weight:700;font-size:30px;letter-spacing:3px;color:var(--ink)}
.brand-tagline{position:absolute;left:118px;top:59px;font-size:13px;color:var(--white)}

.top-links{position:absolute;right:108px;top:9px;display:flex;list-style:none;font-size:12px;font-weight:700;color:var(--white)}
.top-links li{padding:0 10px;border-left:1px solid rgba(255,255,255,.7);line-height:14px}
.top-links li:first-child{border-left:0}
.top-links li:last-child{padding-right:0}

.header-card{position:absolute;top:35px;height:47px;background:var(--white);padding:6px 11px;box-shadow:0 1px 2px rgba(0,0,0,.25)}
.header-card .label{font-family:"Oswald",sans-serif;font-size:15px;color:var(--ink);line-height:18px;display:block}
.header-card .sub{font-family:"Oswald",sans-serif;font-size:11.5px;color:var(--accent);line-height:16px;display:block}
.chat{left:824px;width:111px}
.phones{left:952px;width:142px}
.phones svg{position:absolute;right:10px;top:19px}

.main-nav{position:absolute;left:75px;top:93px;width:1041px;height:42px;border-radius:4px;
  background:linear-gradient(#474747,var(--nav) 50%,var(--nav-dark));box-shadow:0 2px 3px rgba(0,0,0,.3);display:flex;align-items:center}
.main-nav ul{display:flex;list-style:none;height:100%}
.main-nav li{font-family:"Oswald",sans-serif;font-size:12.5px;color:var(--nav-text);padding:0 12px;display:flex;align-items:center;
  border-right:1px solid #262626;box-shadow:1px 0 0 #555}
.main-nav li:first-child{padding-left:20px}
.search{position:absolute;right:10px;top:9px;width:153px;height:24px;background:#2c2c2c;border:1px solid #222;border-radius:3px;
  box-shadow:inset 0 1px 2px rgba(0,0,0,.5);font-size:11.5px;color:#cfcfcf;padding:5px 8px}
.search svg{position:absolute;right:7px;top:5px}

.hero{position:absolute;left:97px;top:157px;width:742px;height:339px;border-radius:5px;overflow:hidden;box-shadow:0 1px 3px rgba(0,0,0,.3)}
.hero-title{height:53px;background:linear-gradient(#4a4a4a,#2f2f2f);display:flex;justify-content:center;align-items:center}
.hero-title h1{font-family:"Bebas Neue",sans-serif;font-weight:400;font-size:48px;letter-spacing:1px;padding-top:4px;
  background:linear-gradient(#ffe34d,#f6a300);-webkit-background-clip:text;background-clip:text;color:transparent}
.hero-sky{height:202px;background:linear-gradient(#6fa0cc,var(--sky) 45%,#dfeaf2 70%,#c8d9e6)}
.hero-base{height:84px;background:linear-gradient(#d8434a,var(--red) 40%,var(--red-dark))}
.hero-product{position:absolute;left:94px;top:56px;width:128px;height:282px;border-radius:14px;
  background:linear-gradient(90deg,#1d1d1d,#3e3e3e 45%,#151515)}
.hero-copy{position:absolute;right:21px;top:75px;text-align:right;font-family:"Signika",sans-serif;font-weight:600;font-size:28.5px;line-height:30px;
  color:var(--white);-webkit-text-stroke:1px #2f5f93;paint-order:stroke fill;text-shadow:0 0 3px #2f5f93}
.cta{position:absolute;left:354px;top:272px;width:213px;height:51px;border-radius:26px;
  background:linear-gradient(#fff06a,var(--yellow) 45%,var(--yellow-dark));box-shadow:0 2px 3px rgba(0,0,0,.35);
  display:flex;justify-content:center;align-items:center;font-family:"Arimo",Arial,sans-serif;font-weight:700;font-size:31px;color:#2d2416}

.promo{position:absolute;left:864px;width:234px;height:161px;border-radius:4px;overflow:hidden;box-shadow:0 1px 3px rgba(0,0,0,.3)}
.promo-dark{top:159px;background:linear-gradient(135deg,#4a4643,var(--box-dark))}
.promo-light{top:336px;background:linear-gradient(135deg,#9a8d86,var(--box-light))}
.promo h2{position:absolute;left:24px;top:20px;font-family:"Oswald",sans-serif;font-weight:500;font-size:29px;line-height:34px;letter-spacing:-.3px}
.promo-dark h2 .a{color:var(--tan)} .promo-dark h2 .b{color:var(--white)}
.promo-light h2{left:24px} .promo-light h2 .a{color:#3d3d3d} .promo-light h2 .b{color:var(--white)}
.promo p{position:absolute;left:24px;top:62px;width:130px;font-size:13px;line-height:19px;color:var(--white)}
.promo-light p{left:29px;top:63px}
.promo .more{position:absolute;left:23px;width:92px;height:23px;border-radius:12px;font-size:12px;font-weight:700;color:var(--white);
  display:flex;justify-content:center;align-items:center;box-shadow:0 1px 2px rgba(0,0,0,.4)}
.promo-dark .more{top:114px;background:linear-gradient(#e6cfa3,var(--tan));color:#4a3a24}
.promo-light .more{top:111px;background:linear-gradient(#e8504f,var(--red-dark))}
.promo .visual{position:absolute;right:0;bottom:0}
.promo-dark .visual{width:120px;height:108px;background:linear-gradient(#d48a3c,#9c5a22)}
.promo-light .visual{width:100px;height:88px;background:linear-gradient(#1c2a2a,#0d1414)}

.section-title{position:absolute;left:107px;top:528px;font-family:"Oswald",sans-serif;font-weight:500;font-size:19px;color:var(--ink)}
.section-rule{position:absolute;left:97px;top:562px;width:1019px;height:4px;background:#e0e0e0}
</style>
</head>
<body>
<header class="site-header">
  <div class="brand"><span class="brand-name">TRAVESSA</span></div>
  <p class="brand-tagline">Soluções em Automação e Código de barras</p>
  <ul class="top-links"><li>Principal</li><li>Quem Somos</li><li>Entre em Contato</li></ul>
  <div class="header-card chat"><span class="label">CHAT ONLINE</span><span class="sub">CLIQUE AQUI</span></div>
  <div class="header-card phones"><span class="label">TELEFONES</span><span class="sub">TODOS OS ESTADOS</span>
    <svg width="9" height="5" viewBox="0 0 9 5"><path d="M0 0h9L4.5 5z" fill="#3a3a3a"/></svg></div>
</header>

<nav class="main-nav">
  <ul>
    <li>LEITOR DE CÓDIGO DE BARRAS</li><li>IMPRESSORA DE ETIQUETAS</li><li>AUTOMAÇÃO COMERCIAL</li><li>ETIQUETAS</li>
    <li>COLETOR DE DADOS</li><li>IMPRESSORA DE CARTÃO</li><li>MARCAS</li>
  </ul>
  <div class="search">Busca
    <svg width="12" height="12" viewBox="0 0 12 12"><circle cx="5" cy="5" r="3.6" fill="none" stroke="#e6e6e6" stroke-width="1.6"/><path d="M7.6 7.6L11 11" stroke="#e6e6e6" stroke-width="2"/></svg></div>
</nav>

<section class="hero">
  <div class="hero-title"><h1>COLETOR DE DADOS</h1></div>
  <div class="hero-sky"></div>
  <div class="hero-base"></div>
  <div class="hero-product" role="img" aria-label="Coletor de dados portátil com tela e teclado numérico"></div>
  <p class="hero-copy">Computadores móveis com leitor<br>de código de barras, que levam<br>a automação para frente<br>de trabalho.</p>
  <div class="cta">Veja Mais</div>
</section>

<aside class="promo promo-dark">
  <div class="visual" role="img" aria-label="Caixa de papelão para entrega"></div>
  <h2><span class="a">Entrega</span><span class="b">Rápida</span></h2>
  <p>Enviamos sua compra para todo o Brasil.</p>
  <div class="more">Leia Mais</div>
</aside>
<aside class="promo promo-light">
  <div class="visual" role="img" aria-label="Sacola de compras escura"></div>
  <h2><span class="a">Boleto</span><span class="b">Faturado</span></h2>
  <p>Receba seu pedido com os boletos.</p>
  <div class="more">Leia Mais</div>
</aside>

<h3 class="section-title">DESTAQUES</h3>
<div class="section-rule"></div>
</body>
</html>
```